Web design for online activity booking website

Our activity booking website uTrundle.net is looking outdated and needing a loving revamp on its design and STRUCTURE. it was initially created as a destination guide before we modified the homepage slightly to sell activities. So please DON'T RELY on the current website for your design. Now, the focus is ACTIVITY, while guide/ info should come only as secondary.

In other words, we will be doing something very similar to Wandelo.com (a bit crowded for our liking) and FindMyOuting.com. If you could capture the best essences of both, that would be awesome! Besides, we also like roostly.com's simplicity.

SIMPLE, CLEAN, BRIGHT, USER and MOBILE FRIENDLY please :)

We have a new logo created and some wireframes (a few more in progress) so you know the basic components required in each page. These are just rough ideas so please ignore the ratio/size, colours etc and if you have a better way of arranging or simplifying things, please do so :)

Help us make it a website that everyone would love!

Thank you in advance for your time and artistry.

Target Market(s)

Internet savvy travellers between 18-65

Industry/Entity Type

Tourism

Number of Pages Required

5+ page

Requirements
Must have
• SIMPLE, CLEAN feel, USER and MOBILE FRIENDLY please :)
• See attachments for rough structure. Will also need standard pages such as:
• - About Us
• - Contact Us
• - Wishlist etc
• Message from our developer "designer to keep layers in PSD format accurately so html/css code does not need to lead a mess in photoshop"
Nice to have
• UPDATE: We are so thrilled to receive so many web designs but on the other hand, the submissions are getting too generic and everyone's designs is almost looking identical (many look like they are “borrowed” from existing popular websites). This is making the selection and decision process very difficult.
• So instead of sending us more of the very similar homepage design with minor tweaks (which we can do during handover section anyway), please send us a design of more specific page of our website. Please refer job brief, file no. 5 - Product detail page.
• This will give us better idea of your skills and choose the best as winner to work on the rest of our web pages.
Should not have
• No dark background please

```html
<!DOCTYPE html>
<html lang="en">
<head>
<meta charset="utf-8">
<title>uTrundle – Book Activities</title>
<link href="https://fonts.googleapis.com/css2?family=Lato:wght@300;400;700;900&display=swap" rel="stylesheet">
<style>
:root{
  --blue:#1a9be0;
  --blue-dark:#0f6fb8;
  --green:#2db84b;
  --pink:#f0255b;
  --orange:#f39019;
  --text:#333a40;
  --muted:#7d858c;
  --line:#d9dde1;
  --section-gray:#eef1f4;
  --footer:#f1f3f6;
  --white:#ffffff;
  --star:#f6c21c;
}
*{box-sizing:border-box;margin:0;padding:0}
html,body{width:679px;height:1200px;overflow:hidden;background:var(--white)}
body{font-family:"Lato",sans-serif;color:var(--text);position:relative}
.abs{position:absolute}

/* hero */
.hero{left:0;top:0;width:679px;height:219px;background:linear-gradient(180deg,#2c7fd6 0%,#4fa3e6 45%,#6fb6ea 70%,#2c6fb8 100%)}
.hero-photo{left:0;top:0;width:679px;height:219px;background:radial-gradient(ellipse at 20% 60%,rgba(255,255,255,.55),rgba(255,255,255,0) 45%),radial-gradient(ellipse at 55% 25%,rgba(255,255,255,.3),rgba(255,255,255,0) 40%)}
.brand{font-weight:900;font-size:15px;color:var(--white);letter-spacing:-.2px}
.brand-hero{left:118px;top:9px}
.nav{left:398px;top:8px;display:flex;gap:10px;align-items:center}
.nav svg{width:12px;height:12px;fill:var(--white)}
.signup{background:var(--orange);color:var(--white);font-size:5px;font-weight:700;padding:2px 5px;border-radius:1px;margin-left:2px}
.hero-title{left:0;width:679px;top:90px;text-align:center;font-weight:900;font-size:29px;color:var(--white);letter-spacing:-.3px;text-shadow:0 1px 3px rgba(0,0,0,.35)}
.hero-sub{left:237px;top:124px;width:206px;height:20px;background:var(--blue);color:var(--white);font-weight:700;font-size:15px;text-align:center;line-height:20px}
.search-panel{left:122px;top:170px;width:436px;height:31px;background:rgba(255,255,255,.35);border-radius:3px;display:flex;gap:4px;padding:6px 5px 5px 5px}
.field{background:var(--white);height:19px;font-size:6.5px;color:#555;padding:0 4px;display:flex;align-items:center;justify-content:space-between}
.field svg{width:10px;height:10px}
.go{background:var(--green);color:var(--white);font-weight:900;font-size:10px;display:flex;align-items:center;justify-content:center;width:53px;height:21px;margin-top:-1px;border-radius:1px}

/* destinations */
.section-title{left:0;width:679px;text-align:center;font-size:14.5px;color:#444}
.tile{border-radius:1px;overflow:hidden}
.tile-label{position:absolute;left:0;right:0;top:50%;transform:translateY(-50%);text-align:center;color:var(--white);font-size:9.5px;text-shadow:0 1px 2px rgba(0,0,0,.5)}
.tile-actions{position:absolute;left:42px;bottom:8px;display:flex;gap:20px;align-items:center}
.tile-select{width:74px;height:14px;background:var(--white);font-size:4.5px;color:#777;display:flex;align-items:center;justify-content:center;position:relative}
.tile-select::after{content:"";position:absolute;right:5px;top:6px;border:2px solid transparent;border-top:2px solid #333}
.tile-book{width:74px;height:14px;background:var(--green);color:var(--white);font-size:4.5px;display:flex;align-items:center;justify-content:center}
.show-more{left:0;width:679px;top:526px;text-align:center;font-size:5px;font-weight:700;color:var(--blue)}

/* activities */
.activities{left:0;top:567px;width:679px;height:239px;background:var(--section-gray)}
.act-search{left:316px;top:597px;font-size:4.5px;color:#444;display:flex;align-items:center;gap:3px}
.tabs{left:244px;top:609px;display:flex;gap:36px;font-size:5px;color:#555}
.tabs .active{color:var(--orange)}
.card{background:var(--white);box-shadow:0 1px 3px rgba(0,0,0,.12);border-radius:2px}
.card-img{width:100%;height:70px;border-radius:2px 2px 0 0}
.card-name{font-weight:700;font-size:8px;margin:5px 0 0 6px;color:#222}
.card-meta{font-size:3.4px;color:#777;margin:1px 0 0 6px}
.card-desc{font-size:3.4px;color:#999;margin:1px 6px 0 6px;line-height:1.4}
.card-row{display:flex;justify-content:space-between;align-items:center;margin:4px 6px 0 6px}
.price{font-weight:700;font-size:13px;color:var(--pink)}
.price sup{font-size:8px}
.price.green{color:var(--green)}
.stars{font-size:6px;color:var(--star);letter-spacing:.3px}
.stars span{color:#ccc}
.heart{position:absolute;width:15px;height:15px;border-radius:50%;background:var(--pink);display:flex;align-items:center;justify-content:center;border:1.5px solid var(--white)}
.heart.green{background:var(--green)}
.heart svg{width:8px;height:8px;fill:var(--white)}
.book-now{margin:6px 6px 0 6px;height:15px;background:var(--green);color:var(--white);font-size:5px;font-weight:700;display:flex;align-items:center;justify-content:center;border-radius:1px}
.arrow{width:22px;height:22px;border:1px solid #888;border-radius:50%;display:flex;align-items:center;justify-content:center;background:rgba(255,255,255,.4)}
.arrow svg{width:8px;height:8px;stroke:#666;fill:none;stroke-width:1.6}

/* map */
.map{left:0;top:806px;width:679px;height:228px;background:linear-gradient(135deg,#8d8e8c,#a3a39f 50%,#8b8c8a)}
.hotspots{left:118px;top:830px;width:122px;height:148px;background:var(--white);box-shadow:0 1px 4px rgba(0,0,0,.3)}
.hotspots h3{font-weight:400;font-size:6.5px;color:#777;text-align:center;padding:5px 0 4px;border-bottom:1px solid #eee}
.hot-row{display:flex;align-items:center;gap:7px;font-size:4px;color:#333;height:21.8px;padding-left:6px;border-bottom:1px solid #f1f1f1}
.hot-row .stars{font-size:5px;color:var(--orange)}
.popup{left:310px;top:833px;width:212px;height:133px;background:var(--white);box-shadow:0 1px 5px rgba(0,0,0,.35)}
.popup-head{display:flex;gap:7px;padding:7px 8px 0}
.popup-title{font-size:8px;color:#222;line-height:1.2}
.popup-img{position:absolute;left:0;top:35px;width:212px;height:70px;background:linear-gradient(180deg,#8a8f95,#5e6368 60%,#3f4246)}
.popup-overview{position:absolute;left:8px;top:70px;color:var(--white)}
.popup-overview h4{font-weight:400;font-size:10px}
.popup-overview p{font-size:3.6px;line-height:1.35;width:195px}
.popup-foot{position:absolute;left:15px;top:108px;right:14px;display:flex;justify-content:space-between}
.map-search{left:119px;top:998px;width:336px;height:31px;background:rgba(255,255,255,.45);border-radius:2px;display:flex;align-items:center;padding:0 4px;gap:4px}
.map-input{width:169px;height:19px;background:var(--white);font-size:6px;color:#444;display:flex;align-items:center;padding-left:4px}
.map-btn{height:19px;width:53px;background:var(--green);color:var(--white);font-size:8.5px;display:flex;align-items:center;justify-content:center;gap:3px}
.or{font-size:6px;color:#333;margin:0 9px}
.near-btn{height:23px;width:81px;background:var(--orange);color:var(--white);font-size:4.8px;display:flex;align-items:center;justify-content:center;gap:3px;border-radius:2px}

/* newsletter */
.newsletter{left:0;top:1034px;width:679px;height:58px;background:var(--orange)}
.news-title{left:173px;top:1049px;color:var(--white);font-size:11px}
.news-sub{left:173px;top:1063px;color:var(--white);font-size:4.3px;width:160px;line-height:1.3}
.news-form{left:344px;top:1052px;width:162px;height:18px;background:var(--white);display:flex;align-items:center;justify-content:space-between;padding-left:9px;font-size:5.5px;color:#555;border:1px solid #fff}
.news-form span.btn{background:var(--blue);color:var(--white);height:14px;width:54px;display:flex;align-items:center;justify-content:center;font-size:5.5px;margin-right:1px}

/* footer */
.footer{left:0;top:1092px;width:679px;height:108px;background:var(--footer)}
.brand-foot{left:118px;top:1105px;color:var(--orange);font-size:15px}
.legal{left:118px;top:1128px;font-size:5px;color:#666;line-height:1.4}
.fcol{top:1115px;font-size:5px;color:#666}
.fcol h5{font-weight:400;color:var(--blue);font-size:5px;margin-bottom:7px}
.fcol div{margin-bottom:8.6px}
.social{left:525px;top:1115px;font-size:5px;color:var(--blue);text-align:center;width:40px}
.social-grid{display:grid;grid-template-columns:15px 15px;gap:5px 4px;margin-top:5px}
.social-grid i{width:15px;height:15px;border-radius:50%;display:block}
</style>
</head>
<body>

<!-- hero -->
<div class="abs hero" role="img" aria-label="Skydivers in free fall high above the clouds and ocean"></div>
<div class="abs hero-photo"></div>
<div class="abs brand brand-hero">uTrundle</div>
<nav class="abs nav" aria-label="Account">
  <svg viewBox="0 0 24 24"><path d="M12 21 3.5 12.8A5 5 0 0 1 12 6a5 5 0 0 1 8.5 6.8z"/></svg>
  <svg viewBox="0 0 24 24"><path d="M2 4h3l2.5 11h11L21 7H7" fill="none" stroke="#fff" stroke-width="2"/><circle cx="9" cy="19" r="1.8"/><circle cx="17" cy="19" r="1.8"/></svg>
  <svg viewBox="0 0 24 24"><circle cx="12" cy="12" r="9" fill="none" stroke="#fff" stroke-width="2"/><path d="M3 12h18M12 3c3 3 3 15 0 18M12 3c-3 3-3 15 0 18" fill="none" stroke="#fff" stroke-width="1.5"/></svg>
  <svg viewBox="0 0 24 24"><circle cx="12" cy="12" r="10"/><text x="12" y="17" font-size="13" text-anchor="middle" fill="#2c7fd6" font-family="Lato,sans-serif" font-weight="700">$</text></svg>
  <svg viewBox="0 0 24 24"><circle cx="12" cy="12" r="10"/><text x="12" y="17" font-size="13" text-anchor="middle" fill="#2c7fd6" font-family="Lato,sans-serif" font-weight="700">?</text></svg>
  <svg viewBox="0 0 24 24"><circle cx="12" cy="7" r="5"/><path d="M2 23c0-7 20-7 20 0z"/></svg>
  <span class="signup">Sign Up</span>
</nav>
<h1 class="abs hero-title">BOOK ACTIVITIES</h1>
<div class="abs hero-sub">Your Adventure Starts Here!</div>
<form class="abs search-panel">
  <div class="field" style="width:106px">Where to, my friend?</div>
  <div class="field" style="width:107px">What would you like to do?</div>
  <div class="field" style="width:73px;font-size:5px">START DATE
    <svg viewBox="0 0 24 24"><rect x="3" y="5" width="18" height="16" fill="none" stroke="#444" stroke-width="1.6"/><path d="M3 9h18M8 3v4M16 3v4" stroke="#444" stroke-width="1.6"/><text x="12" y="19" font-size="8" text-anchor="middle" fill="#444" font-family="Lato,sans-serif">23</text></svg>
  </div>
  <div class="field" style="width:72px;font-size:5px">ADULT X1</div>
  <div class="go">LET'S GO!</div>
</form>

<!-- destinations -->
<h2 class="abs section-title" style="top:236px">Explore Our Top Destinations</h2>
<div class="abs tile" style="left:139px;top:270px;width:118px;height:118px;background:linear-gradient(160deg,#5aa7d8,#2a8fb0 45%,#5b8a3a)" role="img" aria-label="Coastal town above a turquoise bay"><span class="tile-label">MONTE CARLO</span></div>
<div class="abs tile" style="left:275px;top:270px;width:117px;height:118px;background:linear-gradient(180deg,#8fa7b5,#8a7150 40%,#3d5a63 65%,#c8d2d0)" role="img" aria-label="Waves breaking on a rocky shore"><span class="tile-label">BERMUDA</span></div>
<div class="abs tile" style="left:412px;top:270px;width:118px;height:118px;background:linear-gradient(180deg,#1e8fd8,#6e7a88 40%,#d9a24a 65%,#2c4a70)" role="img" aria-label="Harbour town lit at dusk"><span class="tile-label">ITALY</span></div>
<div class="abs tile" style="left:139px;top:402px;width:253px;height:119px;background:linear-gradient(180deg,#3b3a58,#6a3f55 40%,#2a2c3a 75%,#1d2433)" role="img" aria-label="Coastal cliffs at dusk">
  <svg style="position:absolute;left:120px;top:36px;width:14px;height:14px" viewBox="0 0 24 24"><path d="M14 4l7 7-7 7v-4c-5 0-9 1-11 6 0-7 4-11 11-12z" fill="none" stroke="#fff" stroke-width="1.6"/></svg>
  <span class="tile-label" style="top:60%">MONTEGO BAY</span>
  <div class="tile-actions"><div class="tile-select">ACTIVITIES</div><div class="tile-book">BOOK NOW</div>
  <svg style="width:9px;height:9px" viewBox="0 0 24 24"><circle cx="18" cy="5" r="3" fill="#ccc"/><circle cx="6" cy="12" r="3" fill="#ccc"/><circle cx="18" cy="19" r="3" fill="#ccc"/><path d="M18 5 6 12l12 7" stroke="#ccc" stroke-width="2" fill="none"/></svg></div>
</div>
<div class="abs tile" style="left:412px;top:402px;width:118px;height:119px;background:linear-gradient(180deg,#9bc9b8,#e0b064 30%,#1b7f8c 55%,#0d4f66)" role="img" aria-label="Bay with boats at sunset"><span class="tile-label">NEW YORK</span></div>
<div class="abs show-more">SHOW MORE DESTINATIONS</div>
<svg class="abs" style="left:331px;top:535px;width:17px;height:17px" viewBox="0 0 24 24"><path d="M12 3a9 9 0 1 1-8.5 6" fill="none" stroke="#1a9be0" stroke-width="2.6" stroke-linecap="round"/></svg>

<!-- activities -->
<section class="abs activities"></section>
<h2 class="abs section-title" style="top:573px">Explore Our Top Activities</h2>
<div class="abs act-search"><svg width="6" height="6" viewBox="0 0 24 24"><circle cx="10" cy="10" r="7" fill="none" stroke="#222" stroke-width="3"/><path d="M15 15l7 7" stroke="#222" stroke-width="3"/></svg>Type to search ...</div>
<div class="abs tabs"><span class="active">RECOMMENDED</span><span>DESTINATION</span><span>MOST POPULAR</span></div>

<div class="abs arrow" style="left:88px;top:689px"><svg viewBox="0 0 10 10"><path d="M7 1 3 5l4 4"/></svg></div>
<div class="abs arrow" style="left:569px;top:689px"><svg viewBox="0 0 10 10"><path d="M3 1l4 4-4 4"/></svg></div>

<article class="abs card" style="left:118px;top:626px;width:106px;height:148px">
  <div class="card-img" style="height:71px;background:linear-gradient(180deg,#1b8fd3,#38b0d8 55%,#1f6e9a)" role="img" aria-label="Divers swimming underwater"></div>
  <span class="abs" style="right:4px;top:4px;width:10px;height:10px;border-radius:50%;background:var(--white);font-size:7px;font-weight:700;color:var(--blue);text-align:center;line-height:10px">?</span>
  <span class="heart green" style="right:12px;top:62px"><svg viewBox="0 0 24 24"><path d="M12 21 3.5 12.8A5 5 0 0 1 12 6a5 5 0 0 1 8.5 6.8z"/></svg></span>
  <div class="card-name">Deep Sea Diving</div>
  <div class="card-meta">8 DAYS, 7 NIGHTS TOUR</div>
  <div class="card-desc">Lorem ipsum dolor sit amet, consectetur adipiscing elit.</div>
  <div class="card-row"><span class="price green"><sup>$</sup>873</span><span class="stars">★★★<span>★★</span></span></div>
  <div class="book-now">BOOK NOW</div>
</article>

<article class="abs card" style="left:232px;top:636px;width:105px;height:128px">
  <div class="card-img" style="background:linear-gradient(180deg,#cfe0ea,#b9cbd6 50%,#d8c7a8)" role="img" aria-label="Rider on a horse along a beach"></div>
  <span class="heart" style="right:4px;top:62px"><svg viewBox="0 0 24 24"><path d="M12 21 3.5 12.8A5 5 0 0 1 12 6a5 5 0 0 1 8.5 6.8z"/></svg></span>
  <div class="card-name">Horseback Riding</div>
  <div class="card-meta">8 DAYS, 7 NIGHTS TOUR</div>
  <div class="card-desc">Lorem ipsum dolor sit amet, consectetur adipiscing elit.</div>
  <div class="card-row"><span class="price"><sup>$</sup>873</span><span class="stars">★★★<span>★★</span></span></div>
</article>

<article class="abs card" style="left:344px;top:636px;width:106px;height:128px">
  <div class="card-img" style="background:linear-gradient(160deg,#3e6d2c,#7aa04a 50%,#2f5a24)" role="img" aria-label="Zip line through the rainforest"></div>
  <span class="heart" style="right:4px;top:62px"><svg viewBox="0 0 24 24"><path d="M12 21 3.5 12.8A5 5 0 0 1 12 6a5 5 0 0 1 8.5 6.8z"/></svg></span>
  <div class="card-name">Amazon Gliding</div>
  <div class="card-meta">8 DAYS, 7 NIGHTS TOUR</div>
  <div class="card-desc">Lorem ipsum dolor sit amet, consectetur adipiscing elit.</div>
  <div class="card-row"><span class="price"><sup>$</sup>873</span><span class="stars">★★★<span>★★</span></span></div>
</article>

<article class="abs card" style="left:457px;top:636px;width:105px;height:128px">
  <div class="card-img" style="background:linear-gradient(180deg,#7e9a5c,#a7b478 45%,#6c7c48)" role="img" aria-label="Cyclist on a trail between grasses"></div>
  <span class="heart" style="right:4px;top:62px"><svg viewBox="0 0 24 24"><path d="M12 21 3.5 12.8A5 5 0 0 1 12 6a5 5 0 0 1 8.5 6.8z"/></svg></span>
  <div class="card-name">Biking in Negril</div>
  <div class="card-meta">8 DAYS, 7 NIGHTS TOUR</div>
  <div class="card-desc">Lorem ipsum dolor sit amet, consectetur adipiscing elit.</div>
  <div class="card-row"><span class="price"><sup>$</sup>873</span><span class="stars">★★★<span>★★</span></span></div>
</article>

<!-- map -->
<div class="abs map" role="img" aria-label="Street map of the city with activity hot spots"></div>
<svg class="abs" style="left:258px;top:841px;width:22px;height:30px" viewBox="0 0 22 30"><path d="M11 29C4 19 1 15 1 10a10 10 0 0 1 20 0c0 5-3 9-10 19z" fill="#7b2c7a" stroke="#fff" stroke-width="1.5"/><circle cx="11" cy="10" r="6" fill="#fff"/><text x="11" y="13" font-size="8" text-anchor="middle" fill="#7b2c7a">★</text></svg>
<svg class="abs" style="left:537px;top:873px;width:22px;height:30px" viewBox="0 0 22 30"><path d="M11 29C4 19 1 15 1 10a10 10 0 0 1 20 0c0 5-3 9-10 19z" fill="#e0254f" stroke="#fff" stroke-width="1.5"/><circle cx="11" cy="10" r="6" fill="#fff"/><path d="M11 14 7.5 10.5a2 2 0 0 1 3.5-2.2 2 2 0 0 1 3.5 2.2z" fill="#e0254f"/></svg>

<aside class="abs hotspots">
  <h3>Activities Hot Spot</h3>
  <div class="hot-row"><span class="stars">★★★★★</span>Top things to do in Tenerife</div>
  <div class="hot-row"><span class="stars">★★★★★</span>Top things to do in Barcelona</div>
  <div class="hot-row"><span class="stars">★★★★★</span>Top things to do in Paris</div>
  <div class="hot-row"><span class="stars">★★★★★</span>Top things to do in London</div>
  <div class="hot-row"><span class="stars">★★★★★</span>Top things to do in Berlin</div>
  <div class="hot-row"><span class="stars">★★★★★</span>Top things to do in Kuala</div>
</aside>

<div class="abs popup">
  <div class="popup-head">
    <svg width="16" height="14" viewBox="0 0 24 22"><path d="M12 21 2.5 11.8A5.5 5.5 0 0 1 12 4a5.5 5.5 0 0 1 9.5 7.8z" fill="#777"/></svg>
    <div class="popup-title">Spellbound: Castleworth Film Studio Tour<br>London, England</div>
    <svg width="9" height="9" viewBox="0 0 10 10" style="margin-left:auto"><path d="M1 1l8 8M9 1 1 9" stroke="#888" stroke-width="1.2"/></svg>
  </div>
  <div class="popup-img" role="img" aria-label="City street outside the film studio"></div>
  <div class="popup-overview"><h4>Overview</h4><p>Take the bus from central London for this full-day studio visit. Walk behind the scenes where the famous film series was made, and see the sets, props and costumes up close.</p></div>
  <div class="popup-foot">
    <div><span class="stars" style="font-size:6px">★★★<span>★★</span></span><div style="font-size:4px;color:#444;margin-top:2px">◷ Duration: 7 hours</div></div>
    <div style="display:flex;gap:14px;align-items:flex-end"><div style="text-align:right"><div style="font-size:3.5px;color:#999">from</div><div class="price green" style="font-size:11px"><sup style="font-size:7px">$</sup>78</div></div>
    <svg width="9" height="9" viewBox="0 0 10 10" style="margin-bottom:5px"><path d="M1 3l4 4 4-4" fill="none" stroke="#1a9be0" stroke-width="1.5"/></svg></div>
  </div>
</div>

<form class="abs map-search">
  <div class="map-input">Search for hotspot by town, postcode etc.</div>
  <div class="map-btn"><svg width="10" height="10" viewBox="0 0 24 24"><circle cx="10" cy="10" r="7" fill="none" stroke="#fff" stroke-width="2.4"/><path d="M15 15l7 7" stroke="#fff" stroke-width="2.4"/></svg>Search</div>
  <span class="or">or</span>
  <div class="near-btn"><svg width="9" height="9" viewBox="0 0 24 24"><circle cx="12" cy="12" r="10" fill="none" stroke="#fff" stroke-width="2"/><path d="M8 16l3-7 5-1-3 7z" fill="#fff"/></svg>Find a Hot spot near me</div>
</form>

<!-- newsletter -->
<div class="abs newsletter"></div>
<div class="abs news-title">Subscribe to our Newsletter</div>
<div class="abs news-sub">Discover exciting travel tips, city guides, and top deals every week on uTrundle.</div>
<form class="abs news-form"><span>enter your email here</span><span class="btn">SUBSCRIBE</span></form>

<!-- footer -->
<footer class="abs footer"></footer>
<div class="abs brand brand-foot">uTrundle</div>
<div class="abs legal">© 2015, uTrundle, LLC.<br>All Rights Reserved.</div>
<div class="abs fcol" style="left:212px"><h5>COMPANY</h5><div>About uTrundle.net</div><div>Corporate info</div><div>Blog</div><div>Careers</div></div>
<div class="abs fcol" style="left:293px"><h5>SUPPORT</h5><div>Contact us</div><div>FAQs</div><div>Legal</div><div>Privacy Policy</div><div>Legal</div></div>
<div class="abs fcol" style="left:365px"><h5>PARTNERSHIPS</h5><div>Supplier sign-up</div><div>Affiliate Programs</div></div>
<div class="abs fcol" style="left:452px"><h5>LOG-INS</h5><div>Customers</div><div>Suppliers</div><div>Affiliates</div></div>
<div class="abs social">SOCIAL
  <div class="social-grid"><i style="background:#1da1f2"></i><i style="background:#3b5998"></i><i style="background:#e52d27"></i><i style="background:#0e76a8"></i></div>
</div>

</body>
</html>
```